PowerPoint template design for TLBavendish Consulting

I'm interested in a PowerPoint template design that incorporates my logo (see attached file). I am an economist who mostly shows charts and tables in Calibri 24 point. Most tables are 4 or 5 columns by 14 or 15 rows so the design should seek to maximize work space on the slide while unmistakably indicating that these are my slides. I will be using the template design when I provide copies of my slides to the audience after the presentation, mostly in PDF format.

Target Market(s)

Mostly non-data types including educators.

Industry/Entity Type

Consulting

Font styles to use
Sans Serif

Colors
00a990
33b8a4
86cfc6

Requirements
Must have
• Looking for something more sleek and subtle, that doesn't take up too much screen real estate and that in some manner incorporates my business card/logo design. The logo doesn't have to be exactly incorporated as is, but it should visually align or mesh. I like the teal and gray/dark gray color palette that is on my business card.
Nice to have
• Open to more transparency/faded coloring, less bold and vivid than subtle background.
Should not have
• The goal is a PP template design that is unmistakably mine but is not so intrusive that it is the focus of every slide. I want the viewer to forget that the slide is coming from me as a consultant and focus on the content of the slide. I'm not using this as part of a marketing or advertising push as much as I am marking my material so folks who refer to the slides at a later date will know that they are mine.

```html
<!DOCTYPE html>
<html lang="en">
<head>
<meta charset="utf-8">
<title>TLBavendish Consulting – Slide Template</title>
<link href="https://fonts.googleapis.com/css2?family=Open+Sans:wght@400;600;700;800&display=swap" rel="stylesheet">
<style>
  :root {
    --teal: #00a990;
    --teal-mid: #33b8a4;
    --teal-light: #86cfc6;
    --teal-dark: #0b7f6f;
    --ink: #2f3437;
    --gray: #6b7175;
    --page: #d9dbdc;
    --slide: #ffffff;
    --rule: #cfd3d4;
  }
  * { box-sizing: border-box; margin: 0; padding: 0; }
  html, body {
    width: 849px; height: 1200px; overflow: hidden;
    background: var(--page);
    font-family: "Open Sans", Arial, sans-serif;
    color: var(--ink);
  }
  .canvas { position: relative; width: 849px; height: 1200px; }
  .slide {
    position: absolute; left: 68px; width: 713px; height: 535px;
    background: var(--slide);
    box-shadow: 0 1px 4px rgba(0,0,0,.18);
    overflow: hidden;
  }
  .slide--about { top: 30px; }
  .slide--who { top: 600px; }

  .slide-header { position: absolute; left: 16px; top: 12px; padding-left: 12px; border-left: 5px solid var(--teal); }
  .slide-header__title { font-size: 11px; font-weight: 700; letter-spacing: .3px; color: var(--ink); }
  .slide-header__date { font-size: 10px; color: var(--teal); margin-top: 3px; }

  .slide-title { position: absolute; left: 30px; top: 58px; font-size: 30px; font-weight: 800; color: var(--teal); letter-spacing: .5px; }

  .photo {
    position: absolute; left: 232px; top: 108px; width: 470px; height: 345px;
    background: linear-gradient(90deg, #ffffff 0%, #eef1f2 25%, #cdd6da 65%, #a9b5bb 100%);
  }

  .partners { position: absolute; left: 30px; top: 145px; width: 290px; }
  .partners__we { font-size: 20px; color: var(--teal-light); font-weight: 600; }
  .partners__best { font-size: 27px; color: var(--teal-mid); font-weight: 600; line-height: 1.1; }
  .partners__word { font-size: 40px; color: var(--teal-dark); font-weight: 700; line-height: 1.05; }
  .partners__text { margin-top: 12px; font-size: 13px; font-weight: 600; line-height: 1.3; color: var(--ink); }

  .footer-rule { position: absolute; left: 0; right: 0; bottom: 50px; height: 1px; background: var(--rule); }
  .brand {
    position: absolute; right: 14px; bottom: 12px;
    display: flex; align-items: center; gap: 6px;
    background: #4a5054; padding: 5px 10px;
  }
  .brand__mark { width: 14px; height: 14px; background: var(--teal); }
  .brand__name { font-size: 14px; font-weight: 700; color: #ffffff; }

  .title-rule { position: absolute; left: 30px; right: 30px; top: 110px; height: 1px; background: var(--rule); }
  .points { position: absolute; left: 40px; top: 140px; width: 640px; display: grid; grid-template-columns: 1fr 1fr; column-gap: 40px; row-gap: 26px; }
  .point__head { display: flex; align-items: center; gap: 10px; }
  .point__num { width: 22px; height: 22px; background: var(--teal); color: #fff; font-size: 12px; font-weight: 700; display: flex; align-items: center; justify-content: center; }
  .point__title { font-size: 18px; font-weight: 700; color: var(--teal); }
  .point__text { margin: 6px 0 0 32px; font-size: 10.5px; line-height: 1.35; color: var(--gray); }
</style>
</head>
<body>
<div class="canvas">

  <section class="slide slide--about">
    <header class="slide-header">
      <div class="slide-header__title">LABOR MARKET ECONOMIST AND SPEAKER PAR EXCELLENCE</div>
      <div class="slide-header__date">July 2015</div>
    </header>
    <h1 class="slide-title">ABOUT US</h1>
    <div class="photo" role="img" aria-label="Photo of three colleagues gathered around a laptop in a bright office"></div>
    <div class="partners">
      <div class="partners__we">WE ARE</div>
      <div class="partners__best">YOUR BEST</div>
      <div class="partners__word">PARTNERS</div>
      <p class="partners__text">Financial Reporting to Investors, Creditors, and Boards Cash Management/Monitoring, including budgeting, analysis, forecasting, and KPIs US Commodity Tax Compliance Cleanup of historical books, and management of bookkeeping Process implementation and improvement Internal control implementation</p>
    </div>
    <div class="footer-rule"></div>
    <div class="brand"><span class="brand__mark"></span><span class="brand__name">TLBavendish</span></div>
  </section>

  <section class="slide slide--who">
    <header class="slide-header">
      <div class="slide-header__title">LABOR MARKET ECONOMIST AND SPEAKER PAR EXCELLENCE</div>
      <div class="slide-header__date">July 2015</div>
    </header>
    <h1 class="slide-title">WHO WE ARE</h1>
    <div class="title-rule"></div>
    <div class="points">
      <div class="point"><div class="point__head"><span class="point__num">1</span><span class="point__title">NUMBER ONE</span></div><p class="point__text">The Southeast Center was established in 1991 as one of a select number of agricultural research centers funded by the United States</p></div>
      <div class="point"><div class="point__head"><span class="point__num">1</span><span class="point__title">NUMBER ONE</span></div><p class="point__text">The Southeast Center was established in 1991 as one of a select number of agricultural research centers funded by the United States</p></div>
      <div class="point"><div class="point__head"><span class="point__num">2</span><span class="point__title">NUMBER TWO</span></div><p class="point__text">The Southeast Center was established in 1991 as one of a select number of agricultural research centers funded by the United States</p></div>
      <div class="point"><div class="point__head"><span class="point__num">2</span><span class="point__title">NUMBER TWO</span></div><p class="point__text">The Southeast Center was established in 1991 as one of a select number of agricultural research centers funded by the United States</p></div>
      <div class="point"><div class="point__head"><span class="point__num">3</span><span class="point__title">NUMBER THREE</span></div><p class="point__text">The Southeast Center was established in 1991 as one of a select number of agricultural research centers funded by the United States</p></div>
      <div class="point"><div class="point__head"><span class="point__num">3</span><span class="point__title">NUMBER THREE</span></div><p class="point__text">The Southeast Center was established in 1991 as one of a select number of agricultural research centers funded by the United States</p></div>
    </div>
    <div class="footer-rule"></div>
    <div class="brand"><span class="brand__mark"></span><span class="brand__name">TLBavendish</span></div>
  </section>

</div>
</body>
</html>
```